Rebrand of an existing product label

We are looking for a new design / label for our body lotion. Attached is the current product label. We have this product available in Retinol, Collagen, Hyaluronic Acid, Vitamin C, and Coconut. The brand should reflect a clinical, trustworthy look. We also want to include on the label that the product contains Dead Sea Minerals. Attached is the dieline for the label for the jar and the top. This jar is the packaging that needs to be used for this project.
Updates

Target Market(s)

40+

Requirements
Must have
• Ingredient callouts on the front + benefits. Ex- Vitamin C Brightening Cream

```html
<!DOCTYPE html>
<html lang="en">
<head>
<meta charset="utf-8">
<title>Avelle Moisturizing Cream Labels</title>
<link href="https://fonts.googleapis.com/css2?family=Lato:wght@300;400;700;900&display=swap" rel="stylesheet">
<style>
  :root {
    --canvas-bg: #eceeed;
    --label-bg: #fbfbfb;
    --ink: #3a3a3a;
    --ink-soft: #7a7a7a;
    --collagen: #c07a9c;
    --collagen-light: #e2b5cb;
    --retinol: #c27f34;
    --retinol-light: #e2b46e;
    --coconut: #7f6a64;
    --coconut-light: #b3a29b;
    --hyaluron: #2b7a77;
    --hyaluron-light: #6fb0ab;
    --vitamin: #cc8d26;
    --vitamin-light: #e9bb55;
  }
  * { box-sizing: border-box; margin: 0; padding: 0; }
  html, body { width: 1200px; height: 636px; overflow: hidden; }
  body { background: var(--canvas-bg); font-family: "Lato", sans-serif; color: var(--ink); }

  .canvas { position: relative; width: 1200px; height: 636px; }

  .label {
    position: absolute;
    width: 270px;
    height: 164px;
    padding: 16px 20px;
    background: var(--label-bg);
    border-radius: 14px;
    box-shadow: 0 6px 18px rgba(0,0,0,0.07);
  }
  .label--collagen { left: 25px;  top: 88px;  --accent: var(--collagen); --accent-light: var(--collagen-light); }
  .label--retinol  { left: 465px; top: 88px;  --accent: var(--retinol);  --accent-light: var(--retinol-light); }
  .label--coconut  { left: 905px; top: 88px;  --accent: var(--coconut);  --accent-light: var(--coconut-light); }
  .label--hyaluron { left: 245px; top: 392px; --accent: var(--hyaluron); --accent-light: var(--hyaluron-light); }
  .label--vitamin  { left: 685px; top: 392px; --accent: var(--vitamin);  --accent-light: var(--vitamin-light); }

  .brand {
    display: flex; align-items: center; justify-content: center; gap: 6px;
    font-size: 13px; font-weight: 400; letter-spacing: 1.5px; color: var(--ink);
  }
  .brand__dot { width: 9px; height: 9px; background: var(--ink); border-radius: 50%; }

  .product-name {
    margin-top: 3px;
    font-size: 37px; font-weight: 400; line-height: 1;
    text-align: center; letter-spacing: 0.5px;
    background: linear-gradient(90deg, var(--accent), var(--accent-light));
    -webkit-background-clip: text; background-clip: text; color: transparent;
  }
  .product-name--wide { letter-spacing: 7px; }

  .product-type {
    margin-top: 5px;
    font-size: 9.5px; font-weight: 900; text-align: center; color: var(--ink); letter-spacing: -0.1px;
  }
  .benefit-band {
    margin-top: 4px;
    padding: 2px 6px;
    font-size: 7px; font-weight: 400; letter-spacing: 0.8px; text-transform: uppercase;
    color: #fff; text-align: center;
    background: linear-gradient(90deg, var(--accent), var(--accent-light));
  }
  .size-line {
    margin-top: 6px;
    font-size: 7.5px; letter-spacing: 0.6px; color: var(--ink); text-align: center;
  }
  .footer-line {
    margin-top: 6px;
    display: flex; align-items: center; justify-content: space-between;
    font-size: 8.5px; font-weight: 300; color: var(--ink-soft); letter-spacing: 0.2px;
  }
</style>
</head>
<body>
<main class="canvas">

  <section class="label label--collagen">
    <div class="brand"><span class="brand__dot"></span>AVELLE</div>
    <h2 class="product-name">COLLAGEN</h2>
    <p class="product-type">MOISTURIZING CREAM FACE, NECK &amp; HANDS</p>
    <p class="benefit-band">For radiant, soft &amp; healthier looking skin</p>
    <p class="size-line">FOR FACE, NECK &amp; HANDS &nbsp;|&nbsp; 16.9 FL OZ (500 ML)</p>
    <div class="footer-line"><span>PROFESSIONAL SIZE</span><span>DEAD SEA MINERALS</span></div>
  </section>

  <section class="label label--retinol">
    <div class="brand"><span class="brand__dot"></span>AVELLE</div>
    <h2 class="product-name product-name--wide">RETINOL</h2>
    <p class="product-type">MOISTURIZING CREAM FACE, NECK &amp; HANDS</p>
    <p class="benefit-band">For radiant, soft &amp; healthier looking skin</p>
    <p class="size-line">FOR FACE, NECK &amp; HANDS &nbsp;|&nbsp; 16.9 FL OZ (500 ML)</p>
    <div class="footer-line"><span>PROFESSIONAL SIZE</span><span>DEAD SEA MINERALS</span></div>
  </section>

  <section class="label label--coconut">
    <div class="brand"><span class="brand__dot"></span>AVELLE</div>
    <h2 class="product-name">COCONUT</h2>
    <p class="product-type">MOISTURIZING CREAM FACE, NECK &amp; HANDS</p>
    <p class="benefit-band">For radiant, soft &amp; healthier looking skin</p>
    <p class="size-line">FOR FACE, NECK &amp; HANDS &nbsp;|&nbsp; 16.9 FL OZ (500 ML)</p>
    <div class="footer-line"><span>PROFESSIONAL SIZE</span><span>DEAD SEA MINERALS</span></div>
  </section>

  <section class="label label--hyaluron">
    <div class="brand"><span class="brand__dot"></span>AVELLE</div>
    <h2 class="product-name">HYALURON</h2>
    <p class="product-type">MOISTURIZING CREAM FACE, NECK &amp; HANDS</p>
    <p class="benefit-band">For radiant, soft &amp; healthier looking skin</p>
    <p class="size-line">FOR FACE, NECK &amp; HANDS &nbsp;|&nbsp; 16.9 FL OZ (500 ML)</p>
    <div class="footer-line"><span>PROFESSIONAL SIZE</span><span>DEAD SEA MINERALS</span></div>
  </section>

  <section class="label label--vitamin">
    <div class="brand"><span class="brand__dot"></span>AVELLE</div>
    <h2 class="product-name">VITAMIN C</h2>
    <p class="product-type">MOISTURIZING CREAM FACE, NECK &amp; HANDS</p>
    <p class="benefit-band">For radiant, soft &amp; healthier looking skin</p>
    <p class="size-line">FOR FACE, NECK &amp; HANDS &nbsp;|&nbsp; 16.9 FL OZ (500 ML)</p>
    <div class="footer-line"><span>PROFESSIONAL SIZE</span><span>DEAD SEA MINERALS</span></div>
  </section>

</main>
</body>
</html>
```